Postcard Design for a Church

The postcard is for a church. This will be going to new movers in the area. I would like it to say "Welcome to the Neighborhood!" somewhere on the postcard. You can say something like like "Transitioning to a new community can be very difficult and sometimes overwhelming. Our goal as a church is to assist and help where needed". You can also say something like "if you're looking for a church home and a place where you'll be embraced, we invite you to worship with us and be our special guest". Our Facebook page is Facebook.com/TheHarborHouseTN. Our Twitter is TheHarborHouse. Our website page is www.TheHarborHouseTN.org. You can list the vision of the church which is "Our vision is to save souls, change lives & impact the community". Please list the address of the church being located in the main auditorium of Marrowdale High School. The time is Sundays at 11am. The address is 7385 Kettering Lane, Brambleton, TN 37412. Our colors are purple and gold. You can also say "We're more than a church, we're a family". I would like it to also say something like "Come and Grow With Us!" My name is Pastor Darnell "WT" Okafor. My wife's name is First Lady Lashonda Okafor. I hope all this makes sense and it's not exactly in order, but I would like to see your designs. Thank you.

```html
<!DOCTYPE html>
<html lang="en">
<head>
<meta charset="utf-8">
<title>The Harbor House – Welcome Postcard</title>
<link href="https://fonts.googleapis.com/css2?family=Italianno&family=Sorts+Mill+Goudy:ital@0;1&display=swap" rel="stylesheet">
<style>
  :root {
    --bg: #2a2a2a;
    --gold-light: #f3ecbc;
    --gold: #d9cc84;
    --gold-deep: #b3a34a;
    --purple: #5a2a82;
    --purple-soft: #8a4fa8;
    --purple-deep: #4d2373;
    --ink: #1e1a14;
    --cream: #f1e7b2;
    --white: #ffffff;
    --line: #777777;
  }
  * { margin: 0; padding: 0; box-sizing: border-box; }
  html, body { width: 900px; height: 1200px; overflow: hidden; background: var(--bg); }
  body { position: relative; font-family: "Sorts Mill Goudy", Georgia, serif; }

  .postcard { position: absolute; left: 125px; width: 652px; height: 502px; overflow: hidden; }
  .postcard--front { top: 78px; background: linear-gradient(135deg, var(--gold-light) 0%, var(--gold) 55%, var(--gold-deep) 100%); }
  .postcard--back { top: 645px; background: var(--white); }

  /* front */
  .church-silhouette { position: absolute; left: 285px; top: 45px; width: 367px; height: 457px;
    background: linear-gradient(180deg, rgba(255,255,255,0.18), rgba(255,255,255,0.28)); }
  .brand { position: absolute; left: 40px; top: 30px; width: 140px; text-align: center; }
  .brand__mark { width: 118px; height: 118px; margin: 0 auto; border-radius: 50%;
    background: var(--purple); border: 5px solid var(--gold-light); box-shadow: 0 0 0 3px var(--gold-deep); }
  .brand__name { margin-top: 10px; font-size: 26px; line-height: 1; color: var(--purple); }

  .script { font-family: "Italianno", cursive; color: var(--purple); font-weight: 400; }
  .welcome { position: absolute; left: 235px; top: 62px; font-size: 96px; line-height: 1; }
  .welcome__small { font-family: "Sorts Mill Goudy", Georgia, serif; font-size: 24px; }
  .neighborhood { position: absolute; left: 318px; top: 148px; font-size: 78px; line-height: 1; }

  .tagline { position: absolute; color: var(--ink); line-height: 1; }
  .tagline--more { left: 55px; top: 294px; font-size: 38px; }
  .tagline--than { left: 148px; top: 330px; font-size: 38px; }
  .tagline--church { left: 258px; top: 268px; font-size: 104px; color: var(--purple); }
  .tagline--were { left: 105px; top: 395px; font-size: 60px; }
  .tagline--family { left: 315px; top: 368px; font-size: 104px; color: var(--purple-soft); }

  /* back */
  .photo { position: absolute; left: 0; top: 0; width: 168px; height: 278px;
    background: linear-gradient(180deg, #e6e4de 0%, #5a4a42 60%, #1c1c1c 100%); }
  .panel { position: absolute; left: 0; top: 0; width: 435px; height: 502px;
    background: linear-gradient(90deg, var(--purple-soft) 0%, var(--purple) 60%, var(--purple-deep) 100%);
    clip-path: polygon(168px 0, 435px 0, 435px 502px, 0 502px, 0 278px, 168px 278px); }
  .grow { position: absolute; color: var(--cream); line-height: 1; }
  .grow--come { left: 180px; top: 30px; font-size: 76px; }
  .grow--and { left: 245px; top: 98px; font-size: 18px; font-family: "Sorts Mill Goudy", Georgia, serif; }
  .grow--grow { left: 295px; top: 60px; font-size: 74px; }
  .grow--with { left: 328px; top: 128px; font-size: 21px; font-weight: 700; font-family: "Sorts Mill Goudy", Georgia, serif; }

  .leaders { position: absolute; left: 180px; top: 170px; font-size: 16px; line-height: 24px; color: var(--white); }
  .leaders strong { color: var(--cream); }

  .address { position: absolute; left: 25px; top: 298px; width: 410px; color: var(--white); }
  .address__title { display: inline-block; font-size: 21px; color: var(--cream); border-bottom: 1px solid var(--cream); padding-right: 28px; margin-left: 3px; }
  .address__text { margin-top: 6px; font-size: 14.5px; line-height: 22px; }
  .address__time { color: var(--cream); }

  .contact { position: absolute; left: 18px; top: 410px; list-style: none; color: var(--white); font-size: 16px; line-height: 24px; }
  .contact li { display: flex; align-items: center; gap: 5px; }
  .contact__dot { width: 9px; height: 9px; border-radius: 50%; background: var(--white); }

  .stamp { position: absolute; left: 540px; top: 28px; width: 82px; height: 103px; border: 1px solid var(--ink); }
  .mail-line { position: absolute; left: 460px; width: 160px; height: 1px; background: var(--line); }
</style>
</head>
<body>
  <section class="postcard postcard--front">
    <div class="church-silhouette" role="img" aria-label="Faint church building silhouette with cross"></div>
    <div class="brand">
      <div class="brand__mark"></div>
      <div class="brand__name">The Harbor House</div>
    </div>
    <h1 class="script welcome">Welcome <span class="welcome__small">to the</span></h1>
    <div class="script neighborhood">Neighborhood</div>
    <p class="tagline tagline--more">We're more</p>
    <p class="tagline tagline--than">than a</p>
    <p class="tagline tagline--church">church,</p>
    <p class="tagline tagline--were">we're a</p>
    <p class="tagline tagline--family">family</p>
  </section>

  <section class="postcard postcard--back">
    <div class="photo" role="img" aria-label="Photo of the pastor and first lady standing together"></div>
    <div class="panel"></div>
    <span class="script grow grow--come">Come</span>
    <span class="grow grow--and">and</span>
    <span class="script grow grow--grow">Grow</span>
    <span class="grow grow--with">With Us</span>

    <p class="leaders">My name-<br><strong>Pastor Darnell "WT" Okafor.</strong><br>My wife's name-<br><strong>First Lady Lashonda Okafor.</strong></p>

    <div class="address">
      <h2 class="address__title">Address:</h2>
      <p class="address__text">Church being located in the main auditorium of Marrowdale High School.<br>7385 Kettering Lane, Brambleton, TN 37412<span class="address__time">(Sundays at 11am)</span></p>
    </div>

    <ul class="contact">
      <li><span class="contact__dot"></span>Facebook.com/TheHarborHouseTN</li>
      <li><span class="contact__dot"></span>TheHarborHouse</li>
      <li><span class="contact__dot"></span>www.TheHarborHouseTN.org</li>
    </ul>

    <div class="stamp"></div>
    <div class="mail-line" style="top:190px"></div>
    <div class="mail-line" style="top:228px"></div>
    <div class="mail-line" style="top:270px"></div>
    <div class="mail-line" style="top:311px"></div>
  </section>
</body>
</html>
```